Colorful Live Music Concert Poster for Tin Harbor

Looking for a portrait oriented "poster" promoting the band's upcoming show at Marlow Lounge on Sunday, 3/22 at 8 pm, and social version (square format for Instagram). <br/><br/>Copy:<br/>Tin Harbor<br/>with The Pale Wires<br/><br/>Marlow Lounge <br/>Sunday, March 22<br/>8 pm<br/><br/>Poster must be consistent with band's overall branding seen on www.tinharborband.example and it's Tunevault page at https://music.example.com/artist/7QxRtaWpLeNmVcz2Ks9DuB?si=381fkTsYpWmaGHeLoRqdXC <br/><br/>BUT, we wouldn't mind taking in a slightly updated direction. A good example is the cover for our recent single Glad Today, which is consistent in theme and color palette while updating the design and color at the same time. <br/><br/>The attached files include some band logo art as well as examples of posters done for prior shows. <br/><br/>The posters need not include photos of the band, but if you are so inclined, we've uploaded some selects as well.<br/><br/>Thank you. <br/><br/>Wendell<br/>Tin Harbor

```html
<!DOCTYPE html>
<html lang="en">
<head>
<meta charset="utf-8">
<title>Tin Harbor with The Pale Wires — Marlow Lounge, Sunday March 22</title>
<link rel="stylesheet" href="https://fonts.googleapis.com/css2?family=Barlow:wght@400;600&family=Barlow+Semi+Condensed:wght@400;600&family=Open+Sans:wght@400&display=swap">
<style>
  :root {
    --paper: #f7f7f7;
    --sun: #f9b200;
    --sky: #009fce;
    --ink: #202a55;
    --text: #111111;
    --photo-wall: #ecebea;
    --photo-hair: #9a6a45;
    --photo-shirt: #2a2d36;
    --photo-gold: #e9a730;
  }
  * { margin: 0; padding: 0; box-sizing: border-box; }
  html, body { width: 900px; height: 1200px; overflow: hidden; background: var(--paper); }
  .poster { position: relative; width: 900px; height: 1200px; background: var(--paper); font-family: "Barlow", sans-serif; color: var(--text); }

  .brick { position: absolute; height: 148px; }
  .brick--sun { background: var(--sun); }
  .brick--sky { background: var(--sky); }
  .brick--ink { background: var(--ink); }
  .brick--photo-singer { background: linear-gradient(90deg, var(--photo-wall) 0%, var(--photo-wall) 45%, var(--photo-hair) 62%, #e8c9b0 72%, var(--photo-hair) 84%, var(--photo-wall) 100%); }
  .brick--photo-duo { background: linear-gradient(90deg, #e6e4e2 0%, #cfb6a4 20%, var(--photo-shirt) 45%, var(--photo-hair) 65%, var(--photo-gold) 85%, #ece8e2 100%); }
  .brick--photo-top { background: linear-gradient(90deg, #e8e6e4 0%, var(--photo-hair) 30%, var(--photo-gold) 55%, #dcb08f 85%, #ebe8e5 100%); }
  .brick--photo-guitar { background: linear-gradient(180deg, var(--photo-shirt) 0%, #2c3140 60%, var(--photo-gold) 85%, #d88a1c 100%); }
  .brick--photo-waist { background: linear-gradient(180deg, #e8e6e2 0%, var(--photo-gold) 30%, #efb640 55%, #dcb49a 75%, #2b3345 100%); }
  .brick--photo-pick { background: linear-gradient(135deg, #f0b34a 0%, #e79a26 45%, #d9c3ad 70%, #c98a22 100%); }
  .brick--photo-neck { background: linear-gradient(180deg, #2b2e38 0%, #6d5a52 30%, #3a3738 60%, #8f8e8c 80%, #23262e 100%); }

  .site-url { position: absolute; top: 9px; right: 14px; font-family: "Open Sans", sans-serif; font-size: 15px; color: var(--text); letter-spacing: 0.1px; }

  .headliner { position: absolute; left: 21px; top: 1084px; }
  .band-name { font-family: "Barlow", sans-serif; font-weight: 400; font-size: 42px; letter-spacing: 9px; color: var(--ink); line-height: 1; text-transform: uppercase; }
  .support { margin-top: 6px; font-family: "Barlow", sans-serif; font-weight: 400; font-size: 17px; letter-spacing: 0.5px; line-height: 1; color: var(--ink); }
  .show-date { position: absolute; left: 22px; top: 1157px; font-weight: 600; font-size: 30px; letter-spacing: 0.5px; line-height: 1; color: var(--text); }

  .venue { position: absolute; right: 21px; top: 1090px; text-align: right; line-height: 1.2; font-style: normal; font-family: "Barlow Semi Condensed", sans-serif; }
  .venue__name { font-weight: 600; font-size: 28px; }
  .venue__line { font-weight: 400; font-size: 28px; }
</style>
</head>
<body>
<main class="poster">
  <div class="brick brick--ink" style="top:0;left:0;width:84px;height:111px"></div>
  <div class="brick brick--sun" style="top:0;left:96px;width:398px;height:111px"></div>
  <div class="brick brick--sky" style="top:0;left:506px;width:394px;height:111px"></div>

  <div class="brick brick--sun" style="top:124px;left:0;width:286px"></div>
  <div class="brick brick--sun" style="top:124px;left:298px;width:398px"></div>
  <div class="brick brick--ink" style="top:124px;left:708px;width:192px"></div>

  <div class="brick brick--ink" style="top:284px;left:0;width:98px"></div>
  <div class="brick brick--sun" style="top:284px;left:110px;width:398px"></div>
  <div class="brick brick--photo-singer" style="top:284px;left:521px;width:379px" role="img" aria-label="Band photo: the singer laughing against a pale wall"></div>

  <div class="brick brick--sky" style="top:443px;left:0;width:303px"></div>
  <div class="brick brick--photo-duo" style="top:443px;left:315px;width:398px" role="img" aria-label="Band photo: guitarist in glasses smiling beside the singer in a yellow top"></div>
  <div class="brick brick--photo-top" style="top:443px;left:725px;width:175px" role="img" aria-label="Band photo: the singer's yellow top and hair"></div>

  <div class="brick brick--sky" style="top:604px;left:0;width:98px"></div>
  <div class="brick brick--photo-guitar" style="top:604px;left:109px;width:398px" role="img" aria-label="Band photo: guitarist's dark shirt above an amber electric guitar"></div>
  <div class="brick brick--photo-waist" style="top:604px;left:519px;width:381px" role="img" aria-label="Band photo: the singer seated in a yellow cropped top"></div>

  <div class="brick brick--photo-pick" style="top:764px;left:0;width:310px" role="img" aria-label="Band photo: a hand picking the strings of an amber guitar"></div>
  <div class="brick brick--photo-neck" style="top:764px;left:322px;width:398px" role="img" aria-label="Band photo: a hand on the guitar fretboard over a patterned seat"></div>
  <div class="brick brick--ink" style="top:764px;left:732px;width:168px"></div>

  <div class="brick brick--sun" style="top:924px;left:0;width:117px"></div>
  <div class="brick brick--ink" style="top:924px;left:128px;width:398px"></div>
  <div class="brick brick--sky" style="top:924px;left:539px;width:361px"></div>

  <p class="site-url">www.tinharborband.example</p>

  <div class="headliner">
    <h1 class="band-name">Tin Harbor</h1>
    <p class="support">with The Pale Wires</p>
  </div>
  <p class="show-date">SUNDAY, MARCH 22 8PM</p>

  <address class="venue">
    <div class="venue__name">Marlow Lounge</div>
    <div class="venue__line">418 N Alder Row</div>
    <div class="venue__line">Los Angeles, CA&nbsp;&nbsp;90028</div>
  </address>
</main>
</body>
</html>
```